Business card for femtech company

Nothing too elaborate but elegant and geared towards the mother and baby market. Prefer full-bleed with logo (attached) rear.

```html
<!DOCTYPE html>
<html lang="en">
<head>
<meta charset="utf-8">
<title>nestlyn — business card</title>
<link rel="stylesheet" href="https://fonts.googleapis.com/css2?family=Montserrat:wght@300;400&display=swap">
<style>
  :root {
    --teal: #4fbfb1;
    --grey: #9b9b9b;
    --grey-dark: #7d7d7d;
    --card: #ffffff;
    --backdrop: #e4e4e4;
    --shadow: rgba(0, 0, 0, 0.14);
  }
  * { box-sizing: border-box; margin: 0; padding: 0; }
  html, body {
    width: 1200px;
    height: 675px;
    overflow: hidden;
  }
  body {
    background: var(--backdrop);
    font-family: "Montserrat", sans-serif;
    display: flex;
    align-items: center;
    justify-content: center;
    gap: 70px;
  }
  .card {
    position: relative;
    width: 500px;
    height: 286px;
    background: var(--card);
    box-shadow: 0 8px 24px var(--shadow);
    overflow: hidden;
  }
  .card__edge {
    position: absolute;
    left: 0;
    width: 100%;
    height: 100%;
    top: 0;
  }

  /* front */
  .brand {
    position: absolute;
    display: flex;
    align-items: center;
    gap: 12px;
  }
  .brand__dot {
    border-radius: 50%;
    background: var(--teal);
    flex: none;
  }
  .brand__name {
    font-weight: 400;
    color: var(--teal);
    letter-spacing: 0.5px;
    line-height: 1;
  }
  .card--front .brand { left: 30px; top: 118px; }
  .card--front .brand__dot { width: 46px; height: 46px; }
  .card--front .brand__name { font-size: 36px; }

  .divider {
    position: absolute;
    left: 282px;
    top: 60px;
    width: 1px;
    height: 150px;
    background: var(--grey);
  }
  .contact {
    position: absolute;
    left: 300px;
    top: 60px;
    color: var(--grey);
  }
  .contact__name {
    font-weight: 400;
    font-size: 24px;
    color: var(--teal);
    line-height: 1;
  }
  .contact__role {
    font-weight: 300;
    font-size: 10.5px;
    margin-top: 4px;
    letter-spacing: 0.3px;
  }
  .contact__rule {
    width: 140px;
    height: 1px;
    background: var(--teal);
    margin: 8px 0 10px;
  }
  .contact__list { list-style: none; }
  .contact__item {
    display: flex;
    align-items: center;
    gap: 7px;
    font-size: 11px;
    font-weight: 400;
    letter-spacing: 0.3px;
    line-height: 1;
    margin-bottom: 8px;
  }
  .contact__icon { width: 10px; height: 10px; flex: none; fill: var(--grey-dark); }

  /* back */
  .card--back {
    display: flex;
    align-items: center;
    justify-content: center;
  }
  .card--back .brand { position: static; gap: 16px; }
  .card--back .brand__dot { width: 64px; height: 64px; }
  .card--back .brand__name { font-size: 52px; }
</style>
</head>
<body>

  <section class="card card--front" aria-label="Business card, front">
    <svg class="card__edge" viewBox="0 0 500 286" preserveAspectRatio="none" aria-hidden="true">
      <polygon points="0,0 220,0 0,8" fill="var(--teal)"/>
      <polygon points="240,286 500,272 500,286" fill="var(--grey)"/>
    </svg>

    <div class="brand">
      <span class="brand__dot"></span>
      <span class="brand__name">nestlyn</span>
    </div>

    <span class="divider"></span>

    <div class="contact">
      <h1 class="contact__name">Your Name</h1>
      <p class="contact__role">Co-Founder business</p>
      <div class="contact__rule"></div>
      <ul class="contact__list">
        <li class="contact__item">
          <svg class="contact__icon" viewBox="0 0 10 10" aria-hidden="true"><path d="M5 0a3.4 3.4 0 0 0-3.4 3.4C1.6 6 5 10 5 10s3.4-4 3.4-6.6A3.4 3.4 0 0 0 5 0zm0 4.8a1.4 1.4 0 1 1 0-2.8 1.4 1.4 0 0 1 0 2.8z"/></svg>
          123-Dummy Road
        </li>
        <li class="contact__item">
          <svg class="contact__icon" viewBox="0 0 10 10" aria-hidden="true"><path d="M2 0.4l1.6 2-0.9 1.2c0.6 1.3 1.5 2.2 2.8 2.8l1.2-0.9 2 1.6-0.8 2C4.5 9.1 0.9 5.5 0 1.2z"/></svg>
          07700 900123
        </li>
        <li class="contact__item">
          <svg class="contact__icon" viewBox="0 0 10 10" aria-hidden="true"><path d="M5 0a5 5 0 1 0 0 10A5 5 0 0 0 5 0zm0 1a4 4 0 0 1 2.6 1L6 3.3 4.6 2.6 3 4l1.6 1.6-0.4 2.2L2.4 6.6 1.1 4.3A4 4 0 0 1 5 1z"/></svg>
          www.nestlyn.com
        </li>
        <li class="contact__item">
          <svg class="contact__icon" viewBox="0 0 10 10" aria-hidden="true"><path d="M0 2h10v6H0zm0.8 0.8L5 5.6l4.2-2.8"/></svg>
          @nestlyn
        </li>
      </ul>
    </div>
  </section>

  <section class="card card--back" aria-label="Business card, back">
    <div class="brand">
      <span class="brand__dot"></span>
      <span class="brand__name">nestlyn</span>
    </div>
  </section>

</body>
</html>
```